Business cards and Stationary | Corvel Music Events

Hello! We need business cards and stationery for a new small business in the music industry. "Corvel is a high-end music agency which provides an unparalleled level of talent and personalized service to the realm entertainment, corporate events, and luxury weddings. Here is where the classical meets the contemporary and we can bring your vision to life.Keeping a steady finger on the pulse of current trends and consistently raising the bar for industry standards, Corvel continues to rise to the forefront of the music industry, providing the utmost professional, high-end, elegant, and engaging entertainment in Australia and World-Wide."

Target Market(s)

Class A. high profile corporate business.

Industry/Entity Type

Entertainment

Contact Information for Business Card

Corvel Music Events

Tessa Holloway
Director | Violinist

Level 7, 41 Marlow Street
Sydney, 2000

Website: www.corvelmusicevents.com
Phone number: 0481 352 604
Email: tessa@corvelmusicevents.com

Font styles to use
Serif
Sans Serif
Script

Colors
feeeee
0355a3
f59296
ffffff

Requirements
Nice to have
• Clean and sophisticated would be perfect.
• If there is a way to include the Instagram without being tacky, that would be awesome
• @corvelmusicevents
• Our website and logo have the following fonts:
• The primary logo is inspired and based on a font called BillionScript but the B is completely hand drawn and the rest is customised a bit to work together cohesively
• Monserrat Light - Is the Music part of the logo and as headers in the site
• Open Sans 300 and 400 (Light or Regular) is used mostly as the body text in the site
• If you want to access the website:
• www.corvelmusicevents.com
• username: client
• password: preview

```html
<!DOCTYPE html>
<html lang="en">
<head>
<meta charset="utf-8">
<title>Corvel Music Events — Business Card</title>
<link rel="stylesheet" href="https://fonts.googleapis.com/css2?family=Montserrat:wght@300;400;600&family=Roboto+Condensed:wght@400;500&display=swap">
<style>
  :root {
    --canvas-bg: #e6e1dc;
    --card-pink: #cd9a9c;
    --card-pink-deep: #c08c8f;
    --card-white: #ffffff;
    --ink-light: #ffffff;
    --logo-ink: #c9999b;
    --shadow: rgba(60, 40, 30, 0.22);
  }
  * { margin: 0; padding: 0; box-sizing: border-box; }
  html, body {
    width: 1200px; height: 1040px; overflow: hidden;
    background: var(--canvas-bg);
  }
  .canvas {
    position: relative; width: 1200px; height: 1040px;
  }
  .card {
    position: absolute; left: 220px; width: 760px; height: 460px;
    border-radius: 26px; overflow: hidden;
    box-shadow: 0 10px 28px var(--shadow);
  }
  .card--front { top: 45px; }
  .card--back { top: 545px; background: var(--card-pink); }

  .card__art { position: absolute; inset: 0; }

  .front-logo {
    position: absolute; left: 455px; top: 120px; width: 300px;
    text-align: center;
    font-family: "Montserrat", sans-serif; font-weight: 300;
    font-size: 36px; letter-spacing: 4px; color: var(--logo-ink);
    white-space: nowrap;
  }

  .contact-block {
    position: absolute; left: 44px; bottom: 34px;
    color: var(--ink-light);
    font-family: "Roboto Condensed", "Arial Narrow", sans-serif;
  }
  .contact-block__name {
    font-weight: 500; font-size: 30px; letter-spacing: 0.5px;
    text-transform: uppercase; line-height: 1;
  }
  .contact-block__role {
    font-size: 19px; text-transform: uppercase; margin-top: 4px;
  }
  .contact-block__address {
    font-size: 17px; line-height: 1.3; margin-top: 22px;
  }
  .contact-list { list-style: none; margin-top: 22px; }
  .contact-list__item {
    display: flex; align-items: center; gap: 10px;
    font-size: 17px; line-height: 1.4;
  }
  .contact-list__icon { width: 14px; height: 14px; flex: none; }

  .back-name {
    position: absolute; left: 0; right: 0; top: 180px;
    text-align: center;
    font-family: "Montserrat", sans-serif; font-weight: 300;
    font-size: 64px; letter-spacing: 6px; color: var(--ink-light);
  }
  .back-web {
    position: absolute; left: 0; right: 0; bottom: 40px;
    text-align: center;
    font-family: "Montserrat", sans-serif; font-weight: 400;
    font-size: 17px; letter-spacing: 6px; color: var(--ink-light);
  }
</style>
</head>
<body>
<main class="canvas">

  <section class="card card--front" aria-label="Business card front">
    <svg class="card__art" width="760" height="460" viewBox="0 0 760 460" aria-hidden="true">
      <rect width="760" height="460" fill="var(--card-pink)"/>
      <circle cx="605" cy="140" r="282" fill="none" stroke="var(--card-white)" stroke-width="1.5" opacity="0.8"/>
      <circle cx="605" cy="140" r="270" fill="var(--card-white)"/>
    </svg>

    <div class="front-logo">Corvel Music</div>

    <div class="contact-block">
      <p class="contact-block__name">Tessa Holloway</p>
      <p class="contact-block__role">Director | Violinist</p>
      <p class="contact-block__address">Level 7, 41 Marlow Street<br>Sydney, 2000</p>
      <ul class="contact-list">
        <li class="contact-list__item">
          <svg class="contact-list__icon" viewBox="0 0 14 14" aria-hidden="true"><path d="M3 1 L5.5 1 L6.5 4 L5 5.2 C5.8 7 7 8.2 8.8 9 L10 7.5 L13 8.5 L13 11 C13 12 12 13 11 13 C5.5 12.6 1.4 8.5 1 3 C1 2 2 1 3 1 Z" fill="var(--ink-light)"/></svg>
          0481 352 604
        </li>
        <li class="contact-list__item">
          <svg class="contact-list__icon" viewBox="0 0 14 14" aria-hidden="true"><rect x="3.5" y="1" width="7" height="12" rx="1.2" fill="none" stroke="var(--ink-light)" stroke-width="1.4"/><circle cx="7" cy="11" r="0.8" fill="var(--ink-light)"/></svg>
          0481 352 604
        </li>
        <li class="contact-list__item">
          <svg class="contact-list__icon" viewBox="0 0 14 14" aria-hidden="true"><rect x="1" y="3" width="12" height="8.5" fill="var(--ink-light)"/><path d="M1 3 L7 8 L13 3" fill="none" stroke="var(--card-pink)" stroke-width="1.2"/></svg>
          tessa@corvelmusicevents.com
        </li>
        <li class="contact-list__item">
          <svg class="contact-list__icon" viewBox="0 0 14 14" aria-hidden="true"><circle cx="7" cy="7" r="6" fill="var(--ink-light)"/><path d="M1 7 H13 M7 1 C4.5 4 4.5 10 7 13 M7 1 C9.5 4 9.5 10 7 13" fill="none" stroke="var(--card-pink)" stroke-width="1"/></svg>
          www.corvelmusicevents.com
        </li>
      </ul>
    </div>
  </section>

  <section class="card card--back" aria-label="Business card back">
    <div class="back-name">Corvel</div>
    <p class="back-web">www.corvelmusicevents.com</p>
  </section>

</main>
</body>
</html>
```